New website

We ned to create a new website that reflects more who we are. We are delivering exclusive premium products to our customers and the current website does not reflect our products at all.
We believe in less is more and need a webpage that is clean yet professional and exclusive.

Target Market(s)

Dentistry

Industry/Entity Type

Dental

Number of Pages Required

5+ page

Font styles to use
Sans Serif

Colors

Designer to choose colors to be used in the design.

Requirements
Must have
• Picture gallery
• Nice structure
• Clean layout
Nice to have
• Light fonts
Should not have
• Any italic font styles

```html
<!DOCTYPE html>
<html lang="en">
<head>
<meta charset="utf-8">
<title>Lumadent – Premium Dental Ceramics</title>
<link href="https://fonts.googleapis.com/css2?family=Cabin:wght@400;500;600;700&family=Lato:wght@300;400;700&display=swap" rel="stylesheet">
<style>
:root{
  --blue:#2e74b5;
  --nav-blue:#1466ad;
  --dark:#2b2b2b;
  --red:#e5173f;
  --text:#222;
  --white:#fff;
  --brand-ink:#1d2a44;
}
*{box-sizing:border-box;margin:0;padding:0}
html,body{width:1200px;height:3805px;overflow:hidden}
body{font-family:"Lato",sans-serif;color:var(--text);background:var(--white);position:relative}
section,header,footer,nav,.masthead{position:absolute;left:0;width:1200px}
.abs{position:absolute}
.photo{position:absolute}

.topbar{top:0;height:30px;background:var(--dark);color:var(--white);font-size:14px;z-index:2}
.topbar .call{left:110px;top:7px}
.topbar .mail{left:555px;top:7px;display:flex;align-items:center;gap:8px}
.social{display:flex;gap:8px}
.social span{width:16px;height:16px;border-radius:50%;background:var(--white);display:block}
.topbar .social{right:110px;top:7px}

.masthead{top:30px;height:110px;background:var(--white)}
.brand{position:absolute;left:0;right:0;top:36px;display:flex;justify-content:center;align-items:center;gap:16px}
.brand-mark{width:26px;height:26px;background:var(--red)}
.brand-name{font-family:"Cabin",sans-serif;font-size:30px;letter-spacing:9px;color:var(--brand-ink);font-weight:400;line-height:36px}

.mainnav{top:140px;height:53px;background:var(--nav-blue);display:flex;align-items:center;padding-left:112px}
.mainnav a{color:var(--white);text-decoration:none;font-family:"Cabin",sans-serif;font-weight:700;font-size:16px;padding:0 16px;line-height:53px;height:53px;display:block}
.mainnav a.active{border-bottom:3px solid var(--white);padding:0;margin:0 16px 0 0}

.hero{top:193px;height:492px}
.hero .photo{inset:0;background:linear-gradient(90deg,#dfeef5 0%,#c7e0ec 40%,#b98a68 65%,#8a5c3f 80%,#d9e8ef 100%)}
.hero h1{position:absolute;left:150px;top:120px;width:375px;text-align:center;font-weight:400;font-size:42px;line-height:38px;color:var(--red);letter-spacing:1px}
.hero p{position:absolute;left:110px;top:262px;width:455px;text-align:center;font-size:14px;font-weight:700;line-height:18px;color:#111}
.btn{display:inline-block;border-radius:8px;color:var(--white);font-weight:700;font-size:14px;text-align:center;text-decoration:none}
.btn-blue{position:absolute;left:257px;top:318px;width:157px;height:40px;line-height:40px;background:var(--nav-blue)}
.dots{position:absolute;left:620px;top:436px;display:flex;gap:9px}
.dots span{width:13px;height:13px;border-radius:50%;background:var(--white)}
.dots span.on{background:var(--nav-blue)}

h2.section-title{font-family:"Cabin",sans-serif;font-weight:600;font-size:25px;line-height:30px;color:var(--nav-blue);position:absolute;white-space:nowrap}
h2.section-title::after{content:"";position:absolute;left:0;bottom:-8px;width:46px;height:3px;background:var(--red)}
h2.right-rule::after{left:auto;right:0}
.copy{position:absolute;font-size:14px;line-height:18px;color:var(--text)}
.copy p{margin-bottom:18px}
.btn-red{position:absolute;height:40px;line-height:40px;background:var(--red)}

.welcome{top:685px;height:462px}
.welcome .photo{left:107px;top:58px;width:383px;height:348px;background:radial-gradient(ellipse at 50% 50%,#f4f1ee 0%,#e9c6c3 35%,#c7474f 70%,#e7d4cf 100%)}
.welcome h2{left:528px;top:58px}
.welcome .copy{left:528px;top:118px;width:576px}
.welcome .btn-red{left:528px;top:368px;width:157px}

.gallery{top:1147px;height:540px;background:var(--blue)}
.gallery h2{position:absolute;left:0;right:0;top:32px;text-align:center;font-family:"Cabin",sans-serif;font-weight:600;font-size:27px;color:var(--white)}
.gallery h2::after{content:"";display:block;margin:10px auto 0;width:46px;height:3px;background:var(--red)}
.arrow-btn{position:absolute;top:201px;width:32px;height:32px;border:2px solid var(--white);border-radius:50%}
.arrow-btn svg{position:absolute;left:7px;top:7px}
.card{position:absolute;top:106px;width:236px;text-align:center;color:var(--white)}
.card .photo{position:relative;width:236px;height:210px;background:linear-gradient(180deg,#c4918b 0%,#e9e2d4 55%,#b35b5d 100%)}
.card h3{font-family:"Cabin",sans-serif;font-weight:600;font-size:26px;margin-top:20px}
.card p{font-size:13px;font-weight:700;line-height:15.5px;margin:6px 22px 0}
.card .btn{margin-top:22px;width:110px;height:26px;line-height:26px;font-size:11px;border-radius:4px;background:var(--red)}

.special{top:1687px;height:883px}
.special .services-title{right:637px;top:76px}
.special .services-copy{left:107px;top:140px;width:456px;text-align:right}
.special .photo.dentist{left:606px;top:76px;width:480px;height:333px;background:linear-gradient(120deg,#3d3a3c 0%,#d9b49e 35%,#dfe9ee 65%,#9bb8c7 100%)}
.special .services-btn{left:401px;top:373px;width:157px}
.special .photo.portrait{left:107px;top:477px;width:451px;height:335px;background:radial-gradient(ellipse at 55% 45%,#e4c4ae 0%,#b88a6c 45%,#5c4637 100%)}
.special .smile-title{left:606px;top:475px}
.special .smile-copy{left:606px;top:530px;width:488px}
.special .smile-btn{left:606px;top:774px;width:157px}

.testimonials{top:2570px;height:520px;background:var(--blue);color:var(--white)}
.testimonials h2{position:absolute;left:0;right:0;top:36px;text-align:center;font-family:"Cabin",sans-serif;font-weight:600;font-size:27px}
.testimonials h2::after{content:"";display:block;margin:10px auto 0;width:46px;height:3px;background:var(--red)}
.quote{position:absolute;top:113px;width:300px;text-align:center}
.quote .avatar{width:186px;height:186px;border-radius:50%;margin:0 auto;background:radial-gradient(circle at 50% 40%,#8f8f8f 0%,#3f3f3f 70%,#d0d0d0 100%)}
.quote h4{font-family:"Cabin",sans-serif;font-size:20px;font-weight:700;letter-spacing:1px;margin-top:20px}
.quote h4 span{font-weight:400}
.quote p{font-size:14px;line-height:24px;margin:2px auto 0;width:250px}
.quote .sub{color:#9cc3e6;margin-top:0}
.quote .more{display:inline-flex;align-items:center;gap:6px;font-size:14px;margin-top:6px}

.map{top:3090px;height:373px;background:linear-gradient(135deg,#eef1e8 0%,#e7ecdf 35%,#a8d1ee 45%,#e9ece4 60%,#a8d1ee 80%,#eef0e8 100%)}

.contact{top:3463px;height:282px;background:var(--red);color:var(--white);text-align:center}
.contact h3{position:absolute;left:0;right:0;top:55px;font-family:"Cabin",sans-serif;font-size:20px;font-weight:700}
.contact .lead{position:absolute;left:0;right:0;top:82px;font-size:15px;font-weight:700;line-height:20px}
.contact-item{position:absolute;top:148px;width:300px;text-align:center;font-size:15px;font-weight:700}
.contact-item .icon{width:44px;height:44px;border:2px solid var(--white);border-radius:50%;margin:0 auto 20px;display:flex;align-items:center;justify-content:center}

.footer{top:3745px;height:60px;background:var(--dark);color:var(--white);font-size:15px}
.footer .copyright{left:110px;top:20px}
.footer .social{right:110px;top:22px}
</style>
</head>
<body>

<header class="topbar">
  <div class="abs call">Call Today : 555-0142-7730</div>
  <div class="abs mail">
    <svg width="14" height="10" viewBox="0 0 14 10"><rect x="0.5" y="0.5" width="13" height="9" fill="#fff"/><path d="M0.5 0.5 7 6 13.5 0.5" fill="none" stroke="#2b2b2b"/></svg>
    hello@lumadent.com
  </div>
  <div class="abs social"><span></span><span></span><span></span><span></span><span></span></div>
</header>

<div class="masthead">
  <div class="brand"><span class="brand-mark"></span><span class="brand-name">LUMADENT</span></div>
</div>

<nav class="mainnav">
  <a href="#" class="active">WELCOME</a>
  <a href="#">PRODUCTS</a>
  <a href="#">SPECIAL SERVICES</a>
  <a href="#">SMILE GALLERY</a>
  <a href="#">THE COMPANY</a>
  <a href="#">SHADE ANALYSIS</a>
  <a href="#">CONTACT</a>
</nav>

<section class="hero">
  <div class="photo" role="img" aria-label="Smiling woman with bright white teeth on a light blue background"></div>
  <h1>LUMADENT<br>&amp;<br>EXPERIENCE</h1>
  <p>Lorem Ipsum is simply dummy text of the printing and industry.<br>Lorem Ipsum has been the industry's</p>
  <a href="#" class="btn btn-blue">Read More..</a>
  <div class="dots"><span class="on"></span><span></span><span></span><span></span><span></span></div>
</section>

<section class="welcome">
  <div class="photo" role="img" aria-label="Close-up of a smile with white teeth and red lips"></div>
  <h2 class="section-title">Welcome to lumadent</h2>
  <div class="copy">
    <p>Who designed this Smile?</p>
    <p>Lumadent smiles has a very distinctive appearance and character.<br>Both these Lumadent features owe as much to their owners as to our dental artisans, because in the final analysis, people who buy a new smile also designs them.</p>
    <p>Inevitably, the greater the demands a smile has to meet, the lower the lowest denominator.</p>
    <p>That's why standard production line smiles have such little character. With our high strength ceramics our aim has never been to create less expensive smiles for the majority, but the perfect smile for few.<br>Isn't it time you joined the few?</p>
  </div>
  <a href="#" class="btn btn-red">Read More..</a>
</section>

<section class="gallery">
  <h2>Product Gallery</h2>
  <div class="arrow-btn" style="left:45px"><svg width="14" height="14" viewBox="0 0 14 14"><path d="M9 2 4 7 9 12" fill="none" stroke="#fff" stroke-width="2.5"/></svg></div>
  <div class="arrow-btn" style="left:1131px"><svg width="14" height="14" viewBox="0 0 14 14"><path d="M5 2 10 7 5 12" fill="none" stroke="#fff" stroke-width="2.5"/></svg></div>

  <div class="card" style="left:107px">
    <div class="photo" role="img" aria-label="Close-up of teeth restored with veneers"></div>
    <h3>Veneers</h3>
    <p>Lorem Ipsum is simply dummy printing and typesetting industry. has been the industry's ever since the 1500s,</p>
    <a href="#" class="btn">Read More..</a>
  </div>
  <div class="card" style="left:360px">
    <div class="photo" role="img" aria-label="Close-up of teeth restored with pressed ceramic"></div>
    <h3>Cera-Press</h3>
    <p>Lorem Ipsum is simply dummy printing and typesetting industry. has been the industry's ever since the 1500s,</p>
    <a href="#" class="btn">Read More..</a>
  </div>
  <div class="card" style="left:611px">
    <div class="photo" role="img" aria-label="Close-up of white composite front teeth" style="background:linear-gradient(180deg,#d9d4cc 0%,#f5f3ee 50%,#9a8f86 100%)"></div>
    <h3>Luma Gradient</h3>
    <p>Lorem Ipsum is simply dummy printing and typesetting industry. has been the industry's ever since the 1500s,</p>
    <a href="#" class="btn">Read More..</a>
  </div>
  <div class="card" style="left:863px">
    <div class="photo" role="img" aria-label="Dental implant bridge model" style="background:linear-gradient(180deg,#c9c6c2 0%,#ece6dc 45%,#d98c92 100%)"></div>
    <h3>Implants</h3>
    <p>Lorem Ipsum is simply dummy printing and typesetting industry. has been the industry's ever since the 1500s,</p>
    <a href="#" class="btn">Read More..</a>
  </div>
</section>

<section class="special">
  <h2 class="section-title right-rule services-title">Special Services</h2>
  <div class="copy services-copy">
    <p>Lumadent ensures exact teeth reconstruction, individual service of the customer and technical information. We can also offer our customers additional service on favorable terms.The below specified additional services are only a part of what we can offer to you andyour patients</p>
    <p>Lumadent Cosmetic Imaging is the first step in creating a blueprint for success. The patient can see the final result before taking any decisions.<br>Click the links in the menu above to learn more!</p>
  </div>
  <div class="photo dentist" role="img" aria-label="Patient smiling in the dental chair during a check-up"></div>
  <a href="#" class="btn btn-red services-btn">Read More..</a>

  <div class="photo portrait" role="img" aria-label="Portrait of a smiling young woman"></div>
  <h2 class="section-title smile-title">Smile Gallery</h2>
  <div class="copy smile-copy">
    <p>This patient had problems with seveere crooked teeth that made the smile unaesthetic. Lumadent provided 6 fullceramic veneers to restore the beauty of a natural smile.</p>
    <p>This patient had problems with a gummy smile and minor diastemas between her teeth. To creat a natural looking smile Lumadent provided 4 fullceramic veneers.</p>
    <p>This patient had problems with crooked teeth that made the smile unnatural and unaesthetic. Lumadent provided 8 fullceramic veneers to restore the beauty of a natural apperance and a straight smile.</p>
    <p>Click the links in the menu above to learn more!</p>
  </div>
  <a href="#" class="btn btn-red smile-btn">Read More..</a>
</section>

<section class="testimonials">
  <h2>What our patients say</h2>
  <div class="quote" style="left:73px">
    <div class="avatar" role="img" aria-label="Patient portrait in black and white"></div>
    <h4>NAME, <span>DIRECTOR</span></h4>
    <p>"Lorem ipsum dolor amet conse ctetur dolore elit,sed do eiusmod tempor et dolore magna."</p>
    <p class="sub">Lorem ipsum dolor</p>
    <div class="more">read more... <svg width="18" height="18" viewBox="0 0 18 18"><circle cx="9" cy="9" r="8" fill="none" stroke="#fff" stroke-width="1.5"/><path d="M5 9h8M10 6l3 3-3 3" fill="none" stroke="#fff" stroke-width="1.5"/></svg></div>
  </div>
  <div class="quote" style="left:428px">
    <div class="avatar" role="img" aria-label="Patient portrait in colour" style="background:radial-gradient(circle at 50% 40%,#e0b48c 0%,#a85f2e 60%,#d0d0d0 100%)"></div>
    <h4>NAME, <span>DIRECTOR</span></h4>
    <p>"Lorem ipsum dolor amet conse ctetur dolore elit,sed do eiusmod tempor et dolore magna."</p>
    <p class="sub">Lorem ipsum dolor</p>
    <div class="more">read more... <svg width="18" height="18" viewBox="0 0 18 18"><circle cx="9" cy="9" r="8" fill="none" stroke="#fff" stroke-width="1.5"/><path d="M5 9h8M10 6l3 3-3 3" fill="none" stroke="#fff" stroke-width="1.5"/></svg></div>
  </div>
  <div class="quote" style="left:799px">
    <div class="avatar" role="img" aria-label="Patient portrait in black and white"></div>
    <h4>NAME, <span>DIRECTOR</span></h4>
    <p>"Lorem ipsum dolor amet conse ctetur dolore elit,sed do eiusmod tempor et dolore magna."</p>
    <p class="sub">Lorem ipsum dolor</p>
    <div class="more">read more... <svg width="18" height="18" viewBox="0 0 18 18"><circle cx="9" cy="9" r="8" fill="none" stroke="#fff" stroke-width="1.5"/><path d="M5 9h8M10 6l3 3-3 3" fill="none" stroke="#fff" stroke-width="1.5"/></svg></div>
  </div>
</section>

<section class="map" role="img" aria-label="Map of the clinic location and surrounding coastal region"></section>

<section class="contact">
  <h3>GET IN TOUCH WITH US</h3>
  <div class="lead">Lorem ipsum dolor sit amet consectetur adipiscing<br>elit sed do eiusmod tempor.</div>
  <div class="contact-item" style="left:100px">
    <div class="icon"><svg width="18" height="22" viewBox="0 0 18 22"><path d="M9 21C9 21 2 13 2 8a7 7 0 0 1 14 0c0 5-7 13-7 13z" fill="none" stroke="#fff" stroke-width="2"/><circle cx="9" cy="8" r="2.5" fill="#fff"/></svg></div>
    Linnégatan 14B 211 45 Lundby.
  </div>
  <div class="contact-item" style="left:455px">
    <div class="icon"><svg width="14" height="22" viewBox="0 0 14 22"><rect x="1" y="1" width="12" height="20" rx="2" fill="none" stroke="#fff" stroke-width="2"/><circle cx="7" cy="17" r="1.3" fill="#fff"/></svg></div>
    +46-40-12 34 56
  </div>
  <div class="contact-item" style="left:775px">
    <div class="icon"><svg width="22" height="16" viewBox="0 0 22 16"><rect x="1" y="1" width="20" height="14" rx="1" fill="none" stroke="#fff" stroke-width="2"/><path d="M1 1 11 9 21 1" fill="none" stroke="#fff" stroke-width="2"/></svg></div>
    hello@lumadent.com
  </div>
</section>

<footer class="footer">
  <div class="abs copyright">© 2017 Lumadent - All Rights Reserved</div>
  <div class="abs social"><span></span><span></span><span></span><span></span><span></span></div>
</footer>

</body>
</html>
```